website design for B&T Electric

A portfolio website for a high end commercial and residential electrical contracting company. The current site bandtelectric.example does not represent the current direction but the images in the gallery give you an idea of the work we do. Current logo will be uploaded shortly but is black text on white background.
Target Market(s)
General Contractors, Residential Home Owners, clients intersted in Voskal home automation.
Industry/Entity Type
Electrician
Coding
Coded - Design and coding required
Number of Pages Required
2 page
Font styles to use
Sans Serif
Colors
Designer to choose colors to be used in the design.
Requirements
Must have
- Portfolio section highlighting different service areas and products (Voskal Dwellsync, etc)

```html
<!DOCTYPE html>
<html lang="en">
<head>
<meta charset="utf-8">
<title>B&amp;T Electric</title>
<link rel="stylesheet" href="https://fonts.googleapis.com/css2?family=Montserrat:wght@400;500;600;700&family=Open+Sans:wght@400;600&display=swap">
<style>
:root{
  --gold:#eab308;
  --ink:#1c1c1c;
  --text:#555;
  --light:#f3f3f3;
  --panel:#ececec;
  --dark:#232021;
  --white:#fff;
  --blue:#3a8fc4;
  --green:#3aa64a;
  --navy:#3b4f78;
}
*{box-sizing:border-box;margin:0;padding:0}
html,body{width:1200px;height:3197px;overflow:hidden;background:var(--white)}
body{position:relative;font-family:"Open Sans",Arial,sans-serif;color:var(--text)}
.abs{position:absolute}
h1,h2,h3,h4,.brand,.nav a,.btn,.eyebrow,.label{font-family:"Montserrat",Arial,sans-serif}

/* header */
.site-header{left:0;top:0;width:1200px;height:81px;background:var(--white)}
.brand{left:188px;top:27px;font-size:23px;font-weight:600;color:var(--ink);display:flex;align-items:center;gap:10px}
.brand .dot{width:10px;height:10px;border-radius:50%;background:var(--gold)}
.nav{left:494px;top:33px;display:flex;gap:20px;align-items:center;font-size:12px}
.nav a{color:var(--ink);text-decoration:none;font-weight:500}
.nav a.active{color:var(--gold);border-bottom:2px solid var(--gold);padding:0 6px 8px}
.nav .phone{display:flex;align-items:center;gap:6px;font-size:11px;margin-left:6px}
.nav .search{margin-left:40px}

/* hero */
.hero{left:0;top:81px;width:1200px;height:407px;background:linear-gradient(180deg,#7b6f60 0%,#bcb2a2 45%,#d9d2c6 70%,#6d6558 100%)}
.hero-text{left:0;top:222px;width:1200px;text-align:center;color:var(--white)}
.hero-text h1{font-size:26px;font-weight:600;margin-bottom:6px}
.hero-text p{font-size:13px;line-height:18px}
.btn{display:inline-block;background:var(--gold);color:var(--white);font-size:12px;font-weight:600;padding:9px 30px}
.hero .btn,.hero-text .btn{margin-top:20px}
.arrow-btn{width:30px;height:30px;border-radius:50%;display:flex;align-items:center;justify-content:center}

/* about */
.eyebrow{font-size:10px;font-weight:600;letter-spacing:1.5px;color:var(--gold);text-transform:uppercase}
.about-copy{left:207px;top:576px;width:370px}
.about-copy h2{font-size:21px;line-height:26px;color:var(--ink);font-weight:700;margin:10px 0 16px}
.about-copy p{font-size:11.5px;line-height:17px;margin-bottom:20px}
.about-line{left:632px;top:694px;width:114px;height:1px;background:#777}
.location{left:746px;top:488px;width:349px;height:439px;background:linear-gradient(160deg,#dcb021,#c99d18)}
.location-text{left:772px;top:574px;color:var(--white)}
.location-text h3{font-size:16px;font-weight:600;margin-bottom:12px}
.location-text p{font-size:16px;line-height:20px;opacity:.85}
.location-text .get{font-size:11px;color:var(--ink);margin-top:12px;display:block}

/* gallery */
.gallery-intro{left:0;top:927px;width:273px;height:441px;background:var(--panel)}
.gallery-copy{left:50px;top:1034px;width:190px}
.gallery-copy h2{font-size:19px;line-height:25px;color:var(--ink);font-weight:700;margin:10px 0 10px}
.gallery-copy p{font-size:11px;line-height:17px;margin-bottom:20px}
.more{font-size:10px;color:var(--gold);font-family:"Montserrat",sans-serif;font-weight:600}
.tile{top:927px;width:274px;height:441px}
.tile .photo{position:absolute;left:0;top:0;width:274px;height:347px}
.tile .label{position:absolute;left:0;top:347px;width:274px;height:94px;display:flex;align-items:center;justify-content:center;color:var(--white);font-size:17px;font-weight:500}

/* services */
.services{left:0;top:1368px;width:1200px;height:904px;background:var(--light)}
.services-head{left:0;top:1437px;width:1200px;text-align:center}
.services-head h2{font-size:19px;color:var(--ink);font-weight:700;margin-top:12px}
.timeline{left:599px;top:1535px;width:1px;height:655px;background:#d6d6d6}
.service h3{font-size:15px;line-height:20px;color:var(--ink);font-weight:600;margin-bottom:12px}
.service p{font-size:11px;line-height:18px;margin-bottom:12px}
.num{font-family:"Montserrat",sans-serif;font-size:38px;font-weight:400;color:var(--gold)}
.tick{height:1px;background:#ccc}

/* testimonial */
.testimonial{left:0;top:2272px;width:1095px;height:413px;background:var(--gold)}
.testimonial-side{left:1095px;top:2272px;width:105px;height:413px;background:var(--light)}
.quote{left:0;top:2342px;width:1095px;text-align:center;font-family:"Montserrat",sans-serif;font-size:60px;font-weight:700;color:var(--ink);line-height:50px}
.quote-text{left:350px;top:2410px;width:495px;text-align:center;font-size:11px;line-height:19px;color:var(--white)}
.avatar{border-radius:50%;background:linear-gradient(160deg,#7b7b7b,#2e2e2e);border:3px solid var(--white)}
.author{left:0;top:2586px;width:1095px;text-align:center;color:var(--ink)}
.author h4{font-size:12px;font-weight:600}
.author p{font-size:10px}
.dots{left:1023px;top:2455px;display:flex;flex-direction:column;gap:8px}
.dots span{width:8px;height:8px;border-radius:50%;border:1px solid var(--white)}
.dots span.on{background:var(--white)}

/* footer */
.contact{left:0;top:2685px;width:599px;height:512px;background:var(--dark)}
.contact-copy{left:207px;top:2753px;color:var(--white)}
.contact-copy h2{font-size:19px;font-weight:600;margin:8px 0 28px}
.contact-row{display:flex;gap:22px;margin-bottom:22px}
.contact-row .ico{width:30px;display:flex;justify-content:center;padding-top:4px}
.contact-row h4{font-size:11px;font-weight:600;margin-bottom:4px}
.contact-row p{font-size:11px;line-height:15px;color:#cfcfcf}
.contact-row p.big{font-size:17px}
.socials{display:flex;gap:12px;margin:6px 0 22px}
.socials span{width:24px;height:24px;border-radius:50%;border:1px solid #666}
.socials span.on{background:var(--gold);border-color:var(--gold)}
.copyright{font-size:10px;line-height:15px;color:#aaa}
.map{left:599px;top:2685px;width:601px;height:512px;background:linear-gradient(135deg,#eceae5,#e2e4e0 60%,#dde5dc)}
</style>
</head>
<body>

<header class="abs site-header">
  <div class="abs brand">B&amp;T Electric<span class="dot"></span></div>
  <nav class="abs nav">
    <a class="active" href="#">Home</a>
    <a href="#">Gallery</a>
    <a href="#">Specialty Services</a>
    <a href="#">About</a>
    <a href="#">Contact</a>
    <span class="phone">
      <svg width="12" height="12" viewBox="0 0 24 24"><path fill="#eab308" d="M6.6 10.8a15.1 15.1 0 0 0 6.6 6.6l2.2-2.2a1 1 0 0 1 1-.25 11.4 11.4 0 0 0 3.6.6 1 1 0 0 1 1 1V20a1 1 0 0 1-1 1A17 17 0 0 1 3 4a1 1 0 0 1 1-1h3.5a1 1 0 0 1 1 1 11.4 11.4 0 0 0 .6 3.6 1 1 0 0 1-.25 1z"/></svg>
      (555) 410-7720
    </span>
    <svg class="search" width="12" height="12" viewBox="0 0 24 24"><circle cx="10" cy="10" r="7" fill="none" stroke="#eab308" stroke-width="3"/><path d="M15 15l6 6" stroke="#eab308" stroke-width="3"/></svg>
  </nav>
</header>

<section class="abs hero" role="img" aria-label="Modern living room with lit white wall shelving and a ceiling with recessed lights"></section>
<div class="abs arrow-btn" style="left:121px;top:257px;background:#222">
  <svg width="10" height="10" viewBox="0 0 10 10"><path d="M7 1L3 5l4 4" fill="none" stroke="#fff" stroke-width="1.6"/></svg>
</div>
<div class="abs arrow-btn" style="left:1041px;top:281px;background:var(--gold)">
  <svg width="10" height="10" viewBox="0 0 10 10"><path d="M3 1l4 4-4 4" fill="none" stroke="#fff" stroke-width="1.6"/></svg>
</div>
<div class="abs hero-text">
  <h1>Advanced Electronic Material</h1>
  <p>Applying our technologies to contribute to society<br>and daily life around the world</p>
  <span class="btn">Explore More</span>
</div>

<section>
  <div class="abs about-copy">
    <div class="eyebrow">About Us</div>
    <h2>We offer<br>commercial, residential,<br>light industrial, and<br>agricultural services</h2>
    <p>B&amp;T Electric is a full service electrical contracting shop. We're Voskal Dwellsync and Voskal Motorized Shades certified, as well as an authorized Ventrex generator dealer. We've served the for over 18 years.</p>
    <span class="btn">Explore More</span>
  </div>
  <div class="abs about-line"></div>
  <div class="abs location" role="img" aria-label="Gold-tinted view of the company's shop building"></div>
  <div class="abs location-text">
    <h3>Our Location</h3>
    <p>2215 Ridgeview Road,<br>PO Box 4180,<br>Brennan, ID 83900</p>
    <span class="get">Get direction</span>
  </div>
</section>

<section>
  <div class="abs gallery-intro"></div>
  <div class="abs gallery-copy">
    <div class="eyebrow">Gallery</div>
    <h2>Watch our projects in our photo gallery</h2>
    <p>Lorem ipsum dolor sit amet, ea diceret dissentiet quo. Eum mutat option iisque ut. Vis esse splendide ad. Et adipisci expetendis vis</p>
    <span class="more">Read More &rarr;</span>
  </div>
  <div class="abs tile" style="left:273px">
    <div class="photo" role="img" aria-label="Commercial interior with blue accent lighting and warm lit windows" style="background:linear-gradient(160deg,#1d3a6e,#6a3a1e 55%,#2a1e1a)"></div>
    <div class="label" style="background:var(--navy)">Commercial</div>
  </div>
  <div class="abs tile" style="left:547px">
    <div class="photo" role="img" aria-label="Residential dining room with pendant lights over a white table" style="background:linear-gradient(170deg,#4a4440,#d8d6d2 50%,#9aa59a)"></div>
    <div class="label" style="background:var(--blue)">Residencial</div>
  </div>
  <div class="abs tile" style="left:821px">
    <div class="photo" role="img" aria-label="Landscape patio with outdoor fireplace and string lights at dusk" style="background:linear-gradient(170deg,#1e2124,#4a4035 55%,#2a2a24)"></div>
    <div class="label" style="background:var(--green)">Landscape</div>
  </div>
</section>

<section>
  <div class="abs services"></div>
  <div class="abs services-head">
    <div class="eyebrow">Services</div>
    <h2>We offer 4 types of products</h2>
  </div>
  <div class="abs timeline"></div>

  <div class="abs service" style="left:230px;top:1578px;width:360px">
    <h3>Voskal Dwellsync<br>Certified</h3>
    <p>We're proudly certified to install Voskal Dwellsync systems. Dwellsync gives you complete control over your home lighting with just a few simple buttons.</p>
    <span class="more">Read More &rarr;</span>
  </div>
  <div class="abs tick" style="left:466px;top:1578px;width:1px;height:40px"></div>
  <div class="abs num" style="left:487px;top:1568px">01</div>
  <div class="abs tick" style="left:545px;top:1593px;width:54px"></div>

  <div class="abs service" style="left:750px;top:1728px;width:320px">
    <h3>Voskal Shadeline Motorized<br>Shades Certified</h3>
    <p>Voskal Motorized Shades allow you to automatically adjust the natural lighting in your home or office based on time, preset situations</p>
    <span class="more">Read More &rarr;</span>
  </div>
  <div class="abs tick" style="left:600px;top:1748px;width:58px"></div>
  <div class="abs num" style="left:664px;top:1726px">02</div>
  <div class="abs tick" style="left:733px;top:1728px;width:1px;height:40px"></div>

  <div class="abs service" style="left:230px;top:1893px;width:290px">
    <h3>LED Lighting</h3>
    <p>LED Lighting has rapidly become a functional and affordable option. LED Lighting is a high efficiency energy saving option and the future of lighting.</p>
    <span class="more">Read More &rarr;</span>
  </div>
  <div class="abs tick" style="left:466px;top:1880px;width:1px;height:40px"></div>
  <div class="abs num" style="left:484px;top:1872px">03</div>
  <div class="abs tick" style="left:545px;top:1897px;width:54px"></div>

  <div class="abs service" style="left:750px;top:2032px;width:320px">
    <h3>Emergency Generators</h3>
    <p>Never be without power again&mdash;protect yourself from frozen pipes, inconvenience, and spoiled food. We sell, service, and install quality generators.</p>
    <span class="more">Read More &rarr;</span>
  </div>
  <div class="abs tick" style="left:600px;top:2042px;width:58px"></div>
  <div class="abs num" style="left:662px;top:2020px">04</div>
  <div class="abs tick" style="left:733px;top:2022px;width:1px;height:40px"></div>
</section>

<section>
  <div class="abs testimonial"></div>
  <div class="abs testimonial-side"></div>
  <div class="abs quote">&ldquo;</div>
  <p class="abs quote-text">There are many variations of passages of Lorem Ipsum available, but the majority have suffered alteration in some form, by injected humour, or randomised words which don't look even slightly believable. If you are going to use a passage of Lorem Ipsum, you need to be sure there isn't anything embarrassing hidden.....</p>
  <div class="abs arrow-btn" style="left:207px;top:2447px;width:28px;height:28px;border:1px solid #fff">
    <svg width="8" height="8" viewBox="0 0 10 10"><path d="M1 7l4-4 4 4" fill="none" stroke="#fff" stroke-width="1.6"/></svg>
  </div>
  <div class="abs arrow-btn" style="left:207px;top:2481px;width:28px;height:28px;border:1px solid #fff">
    <svg width="8" height="8" viewBox="0 0 10 10"><path d="M1 3l4 4 4-4" fill="none" stroke="#fff" stroke-width="1.6"/></svg>
  </div>
  <div class="abs avatar" role="img" aria-label="Client portrait" style="left:490px;top:2515px;width:52px;height:52px"></div>
  <div class="abs avatar" role="img" aria-label="Client portrait" style="left:562px;top:2505px;width:72px;height:72px"></div>
  <div class="abs avatar" role="img" aria-label="Client portrait" style="left:654px;top:2515px;width:52px;height:52px"></div>
  <div class="abs author"><h4>Lena Ortis</h4><p>CEO of Company</p></div>
  <div class="abs dots"><span class="on"></span><span></span><span></span></div>
</section>

<footer>
  <div class="abs contact"></div>
  <div class="abs contact-copy">
    <div class="eyebrow">Contact Us</div>
    <h2>Keep in touch</h2>
    <div class="contact-row">
      <div class="ico"><svg width="26" height="26" viewBox="0 0 24 24"><path fill="#5a5a5a" d="M6.6 10.8a15.1 15.1 0 0 0 6.6 6.6l2.2-2.2a1 1 0 0 1 1-.25 11.4 11.4 0 0 0 3.6.6 1 1 0 0 1 1 1V20a1 1 0 0 1-1 1A17 17 0 0 1 3 4a1 1 0 0 1 1-1h3.5a1 1 0 0 1 1 1 11.4 11.4 0 0 0 .6 3.6 1 1 0 0 1-.25 1z"/></svg></div>
      <div><h4>Call Us:</h4><p class="big">(555) 410-7720</p></div>
    </div>
    <div class="contact-row">
      <div class="ico"><svg width="28" height="22" viewBox="0 0 28 22"><rect x="1" y="1" width="26" height="20" fill="#5a5a5a"/><path d="M1 1l13 11L27 1" fill="none" stroke="#232021" stroke-width="2"/></svg></div>
      <div><h4>Email Us:</h4><p>dmarsh@bandtelectric.example<br>cpearce@bandtelectric.example</p></div>
    </div>
    <div class="contact-row">
      <div class="ico"><svg width="28" height="26" viewBox="0 0 28 26"><path fill="#5a5a5a" d="M14 1L1 12h4v13h7v-8h4v8h7V12h4z"/></svg></div>
      <div><h4>Email Us:</h4><p>2215 Ridgeview Road,<br>PO Box 4180,<br>Brennan, ID 83900</p></div>
    </div>
    <div class="socials"><span></span><span class="on"></span><span></span><span></span></div>
    <p class="copyright">&copy; Copyright 2017 B&amp;T Electric.<br>Al Rights Reserved</p>
  </div>
  <div class="abs map" role="img" aria-label="Street map around the shop location with a red marker"></div>
</footer>

</body>
</html>
```